Sticker for Scrap Metal Bin that is placed at customers premises

During the course of our operation, Scrap Metal Bin are place at our customer site for them to dispose scrap metal into the Bin.

Would like to have a sticker for us to paste on the bin.

All scrap bin will be blue color. Attached sample of current sticker on a scrap bin.

Would like one that is clean, simple and eye catching also that the font is much visible unlike the current one that is cramp and small.

Target Market(s)

Businesses

Font styles to use
Serif

Requirements
Must have
• 1) Company Name and Logo
• 2) Contact Details : 9314 5520 / 6283 4057
• 3) Website: www.korvalenmetals.com

```html
<!DOCTYPE html>
<html lang="en">
<head>
<meta charset="utf-8">
<title>Korvalen Metals Recycling – Scrap Metal Bin Sticker</title>
<link href="https://fonts.googleapis.com/css2?family=Michroma&family=Saira+Condensed:wght@600&display=swap" rel="stylesheet">
<style>
  :root {
    --backdrop: #3c7ba3;
    --sticker-black: #231f20;
    --sticker-green: #0b8a45;
    --ink-white: #ffffff;
    --accent-yellow: #f7cf10;
    --ring-dark: #1b1a1a;
  }
  * { margin: 0; padding: 0; box-sizing: border-box; }
  html, body {
    width: 1200px; height: 800px; overflow: hidden;
    background: var(--backdrop);
  }
  .canvas { position: relative; width: 1200px; height: 800px; }
  .sticker {
    position: absolute; left: 168px; top: 112px;
    width: 864px; height: 576px;
    background: var(--sticker-black);
    box-shadow: 6px 8px 14px rgba(0,0,0,0.35);
    color: var(--ink-white);
  }
  .brand-mark {
    position: absolute; left: 385px; top: 38px;
    width: 105px; height: 105px;
    border: 5px solid var(--ink-white);
  }
  .brand-name {
    position: absolute; left: 0; right: 0; top: 172px;
    text-align: center;
    font-family: "Michroma", sans-serif;
    font-size: 30px; line-height: 1;
    letter-spacing: 1px;
  }
  .brand-sub {
    position: absolute; right: 240px; top: 214px;
    font-family: "Michroma", sans-serif;
    font-size: 19px; line-height: 1;
    letter-spacing: 2px;
  }
  .category-band {
    position: absolute; left: 0; top: 271px;
    width: 864px; height: 222px;
    background: var(--sticker-green);
  }
  .material-icon {
    position: absolute; left: 42px; top: 18px;
    width: 182px; height: 182px; border-radius: 50%;
    background: radial-gradient(circle, #ffffff 0%, #ffffff 52%, var(--accent-yellow) 56%, var(--ring-dark) 60%, var(--ring-dark) 100%);
  }
  .band-divider {
    position: absolute; left: 243px; top: 18px;
    width: 6px; height: 196px; border-radius: 3px;
    background: var(--sticker-black);
  }
  .category-title {
    position: absolute; left: 288px; top: 30px;
    font-family: "Michroma", sans-serif;
    font-size: 86px; line-height: 1.0;
    letter-spacing: 3px;
    color: var(--ink-white);
  }
  .contact-bar {
    position: absolute; left: 0; top: 493px;
    width: 864px; height: 83px;
    font-family: "Saira Condensed", sans-serif;
    font-weight: 600; font-size: 34px; line-height: 1;
  }
  .phone-badge {
    position: absolute; left: 42px; top: 14px;
    width: 48px; height: 48px;
  }
  .phone-numbers { position: absolute; left: 102px; top: 20px; }
  .website { position: absolute; right: 44px; top: 20px; }
</style>
</head>
<body>
<div class="canvas">
  <div class="sticker">
    <div class="brand-mark"></div>
    <div class="brand-name">KORVALEN METALS</div>
    <div class="brand-sub">RECYCLING</div>

    <div class="category-band">
      <div class="material-icon" role="img" aria-label="Metal bolt inside circular recycling arrows"></div>
      <div class="band-divider"></div>
      <div class="category-title">SCRAP<br>METAL</div>
    </div>

    <div class="contact-bar">
      <svg class="phone-badge" viewBox="0 0 48 48" aria-hidden="true">
        <circle cx="24" cy="24" r="24" fill="#f7cf10"/>
        <path d="M17 13c1.5-1 3-.5 3.6.8l1.9 4c.5 1 .2 2.1-.7 2.8l-1.6 1.2c1 2.6 3 4.8 5.6 6l1.3-1.5c.7-.8 1.9-1 2.8-.5l3.9 2.1c1.2.7 1.6 2.2.7 3.6-1.3 2.1-3.6 3.1-6 2.4C21.6 33 15.4 26.8 14.1 20c-.5-2.8.8-5.6 2.9-7z" fill="#231f20"/>
      </svg>
      <div class="phone-numbers">:9314 5520 / 6283 4057</div>
      <div class="website">www.korvalenmetals.com</div>
    </div>
  </div>
</div>
</body>
</html>
```